Business Card Design

I need a business card design for my new solo law practice. I practice consumer bankruptcy law.

I would like a simple, functional business card that looks professional but will also be understandable to regular people - not just other lawyers.
Updates

I added a couple of possible logos that can be incorporated

I'm sorry about the confusion, but the suite number for my new office is suite #150. Thanks for your patience

Target Market(s)

the real target market is potential clients

Industry/Entity Type

Business

Contact Information for Business Card

Law Offices of Dorian P. Whitcombe
Dorian P. Whitcombe
Attorney at Law
Bankruptcy Law
487 Mariner Court #150
Fernley, PA 17555
(555) 318-7264 (Phone)
(555) 318-7290 (Fax)
dorianw@fernleydebtrelief.example
fernleydebtrelief.example

Font styles to use
Serif

Requirements
Nice to have
• I've added some possible logos to possible incorporate

```html
<!DOCTYPE html>
<html lang="en">
<head>
<meta charset="utf-8">
<title>Dorian P. Whitcombe – Business Card</title>
<link rel="stylesheet" href="https://fonts.googleapis.com/css2?family=Open+Sans:wght@400&family=Tinos:wght@400&display=swap">
<style>
  :root {
    --bg-base: #6e7394;
    --bg-light: #8a8eab;
    --block: rgba(70, 76, 112, 0.35);
    --block-light: rgba(160, 164, 190, 0.25);
    --glow: #2b3157;
    --ring-white: #ffffff;
    --emblem-top: #8cc43f;
    --emblem-bottom: #eef2e4;
    --gold: #e9dc2c;
    --text: #ffffff;
    --emblem-text: #2f365e;
  }
  html, body {
    margin: 0;
    padding: 0;
    overflow: hidden;
    background: #ffffff;
  }
  .card {
    position: relative;
    width: 1200px;
    height: 696px;
    overflow: hidden;
    background: linear-gradient(180deg, var(--bg-light) 0%, var(--bg-base) 55%, #666b8c 100%);
    font-family: "Open Sans", Arial, sans-serif;
    color: var(--text);
  }
  .backdrop { position: absolute; inset: 0; }
  .contact-block {
    position: absolute;
    left: 30px;
    top: 29px;
    font-size: 20px;
    line-height: 28px;
  }
  .contact-block span { display: block; }
  .contact-block .phone-label { margin-top: 13px; }
  .emblem-name {
    font-family: "Tinos", "Times New Roman", serif;
    font-size: 40px;
    fill: var(--emblem-text);
  }
  .attorney-name {
    position: absolute;
    left: 0;
    width: 1220px;
    top: 452px;
    margin: 0;
    text-align: center;
    font-family: "Tinos", "Times New Roman", serif;
    font-weight: 400;
    font-size: 72px;
    line-height: 80px;
    color: var(--gold);
    text-shadow: 1px 2px 3px rgba(30, 30, 40, 0.55);
  }
  .firm-name {
    position: absolute;
    left: 0;
    width: 1200px;
    top: 532px;
    margin: 0;
    text-align: center;
    font-size: 25px;
    line-height: 34px;
  }
  .practice {
    position: absolute;
    left: 504px;
    top: 567px;
    margin: 0;
    font-size: 24px;
    line-height: 35px;
  }
  .address {
    position: absolute;
    left: 0;
    width: 1200px;
    top: 643px;
    margin: 0;
    text-align: center;
    font-size: 23px;
    line-height: 30px;
  }
</style>
</head>
<body>
  <main class="card">
    <svg class="backdrop" width="1200" height="696" viewBox="0 0 1200 696" aria-hidden="true">
      <defs>
        <radialGradient id="center-glow" cx="614" cy="240" r="340" gradientUnits="userSpaceOnUse">
          <stop offset="0.55" stop-color="var(--glow)" stop-opacity="0.95"/>
          <stop offset="1" stop-color="var(--glow)" stop-opacity="0"/>
        </radialGradient>
        <linearGradient id="emblem-fill" x1="0" y1="0" x2="0" y2="1">
          <stop offset="0.2" stop-color="var(--emblem-top)"/>
          <stop offset="0.85" stop-color="var(--emblem-bottom)"/>
        </linearGradient>
      </defs>
      <rect x="0" y="218" width="175" height="478" fill="var(--block)"/>
      <rect x="102" y="306" width="174" height="390" fill="var(--block)"/>
      <rect x="108" y="522" width="250" height="174" fill="var(--block-light)"/>
      <rect x="355" y="610" width="250" height="86" fill="var(--block)"/>
      <rect x="1038" y="200" width="162" height="496" fill="var(--block)"/>
      <rect x="943" y="290" width="165" height="406" fill="var(--block)"/>
      <rect x="830" y="505" width="270" height="191" fill="var(--block-light)"/>
      <rect x="0" y="0" width="1200" height="26" fill="var(--block-light)"/>
      <circle cx="614" cy="240" r="340" fill="url(#center-glow)"/>
      <circle cx="614" cy="240" r="200" fill="var(--ring-white)"/>
      <circle cx="614" cy="240" r="184" fill="var(--glow)"/>
      <circle cx="614" cy="240" r="160" fill="url(#emblem-fill)" role="img" aria-label="Firm emblem area"/>
      <text class="emblem-name" x="614" y="254" text-anchor="middle">Whitcombe Law</text>
    </svg>

    <div class="contact-block">
      <span class="label">Fax:</span>
      <span class="value">dorianw@fernleydebtrelief.example</span>
      <span class="value">fernleydebtrelief.example</span>
      <span class="label phone-label">Phone:</span>
      <span class="value">(555) 318-7290</span>
    </div>

    <h1 class="attorney-name">Dorian P. Whitcombe</h1>
    <p class="firm-name">Law Offices of Dorian P. Whitcombe</p>
    <p class="practice">Attorney at Law<br>Bankruptcy Law</p>
    <p class="address">487 Mariner Court #150 Fernley, PA 17555 (555) 318-7264</p>
  </main>
</body>
</html>
```